Masculine, visually appealing sales presentation for CPA firm

I have a basic power point that I use for sales presentations and I would like it to be updated to be more appealing and modern.

This is a presentation I give to real estate agents to help them close sales, save taxes, and resolve tax disputes. I would like the powerpoint to be updated to be more visually appealing. I have included the current powerpoint along with some of my logo files.

You don't have to use any of the pictures/clip art that is in the current power point. I only care that the words of the powerpoint make it to the new version.

Target Market(s)

Realtors, Real Estate Agents

Industry/Entity Type

Accounting

Requirements
Must have
• Visually appealing. I don't want it to look like I just took a template and made a normal powerpoint out of it. It should look custom.
Should not have
• Anything unprofessional, anything inconsistent with my brand

```html
<!DOCTYPE html>
<html lang="en">
<head>
<meta charset="utf-8">
<title>Free Consultation – Dale Whitford, CPA</title>
<link rel="stylesheet" href="https://fonts.googleapis.com/css2?family=Anton&family=Roboto+Condensed:wght@700&family=Tinos&display=swap">
<style>
  :root {
    --navy: #0f1f35;
    --alert-red: #ff0a0a;
    --ink: #0f1f35;
    --slate-light: #f3f6f9;
    --slate-mid: #d6dde4;
    --slate-edge: #b9c3cd;
    --art-light: #eef0f2;
    --art-mid: #cfd5da;
    --mascot-tone: #3b3a3c;
  }
  html, body {
    margin: 0;
    padding: 0;
    overflow: hidden;
  }
  body {
    width: 1200px;
    height: 900px;
  }
  .slide {
    position: relative;
    width: 1200px;
    height: 900px;
    overflow: hidden;
    background:
      radial-gradient(ellipse 70% 55% at 50% 55%, #ffffff 0%, rgba(255,255,255,0) 70%),
      linear-gradient(165deg, var(--slate-mid) 0%, var(--slate-light) 45%, var(--slate-mid) 80%, var(--slate-edge) 100%);
  }
  .top-strip {
    position: absolute;
    left: 0; top: 0;
    width: 1200px; height: 50px;
    background: linear-gradient(90deg, #e6eaee, #c9d1d9);
  }
  .header-band {
    position: absolute;
    left: 0; top: 50px;
    width: 1200px; height: 166px;
    background: var(--navy);
  }
  .footer-band {
    position: absolute;
    left: 0; bottom: 0;
    width: 1200px; height: 23px;
    background: var(--navy);
  }
  .property-art {
    position: absolute;
    left: 0; top: 19px;
    width: 335px; height: 243px;
    background: linear-gradient(160deg, var(--art-light) 0%, var(--art-mid) 100%);
  }
  .headline {
    position: absolute;
    left: 0; top: 283px;
    width: 1200px;
    margin: 0;
    text-align: center;
    font-family: "Anton", "Impact", sans-serif;
    font-weight: 400;
    font-size: 84px;
    line-height: 1;
    color: var(--alert-red);
    text-indent: -26px;
    white-space: nowrap;
  }
  .advisor-name {
    position: absolute;
    left: 0; top: 426px;
    width: 1200px;
    margin: 0;
    text-align: center;
    font-family: "Tinos", "Times New Roman", serif;
    font-weight: 400;
    font-size: 78px;
    line-height: 1;
    color: var(--ink);
  }
  .advisor-phone {
    position: absolute;
    left: 0; top: 570px;
    width: 1200px;
    margin: 0;
    text-align: center;
    font-family: "Tinos", "Times New Roman", serif;
    font-weight: 400;
    font-size: 82px;
    line-height: 1;
    color: var(--ink);
  }
  .office-address {
    position: absolute;
    left: 0; top: 738px;
    width: 1200px;
    margin: 0;
    text-align: center;
    font-family: "Tinos", "Times New Roman", serif;
    font-size: 22px;
    line-height: 1;
    color: var(--ink);
  }
  .mascot-art {
    position: absolute;
    left: 41px; top: 750px;
    width: 90px; height: 119px;
    background: var(--mascot-tone);
  }
  .org-rule {
    position: absolute;
    left: 650px; top: 834px;
    width: 536px; height: 2px;
    background: var(--ink);
  }
  .org-name {
    position: absolute;
    left: 650px; top: 842px;
    width: 540px;
    margin: 0;
    text-align: center;
    font-family: "Roboto Condensed", "Arial Narrow", sans-serif;
    font-weight: 700;
    font-size: 24px;
    line-height: 1.2;
    letter-spacing: 0.6px;
    color: var(--ink);
    white-space: nowrap;
  }
</style>
</head>
<body>
  <main class="slide">
    <div class="top-strip"></div>
    <div class="header-band"></div>

    <div class="property-art" role="img" aria-label="Illustration of a modern house with a pool and a set of keys"></div>

    <h1 class="headline">CALL FOR A FREE CONSULTATION</h1>
    <p class="advisor-name">Dale Whitford, CPA</p>
    <p class="advisor-phone">(360)555-0142</p>
    <p class="office-address">2210 NE Cedar Ridge Way Ste 300, Vancouver, WA 98684</p>

    <div class="mascot-art" role="img" aria-label="Brand mascot character illustration"></div>

    <div class="org-rule"></div>
    <p class="org-name">Guild of Tax Resolution Advisors©</p>

    <div class="footer-band"></div>
  </main>
</body>
</html>
```